charity helping airline passengers needs web site design

We need a website design (and a logo) for a new charity based in Switzerland. We are helping airline passengers to receive the compensation they are entiteld to by european law from the airlines in cases of delays or denied boarding or cancelled flights. Airlines often try to not pay those compensations so the passengers need assistance in receiving the compensations.

Target Market(s)

Switzerland

Industry/Entity Type

Charity

Logo Text

lindenkrügelhof.ch

Number of Pages Required

1 page

Colors

Designer to choose colors to be used in the design.

```html
<!DOCTYPE html>
<html lang="en">
<head>
<meta charset="utf-8">
<title>Lindenkrügelhof – Helping Airline Passengers</title>
<link rel="stylesheet" href="https://fonts.googleapis.com/css2?family=Poppins:wght@400;500;600;700&family=Open+Sans:ital,wght@0,400;0,600;0,700;1,400&display=swap">
<style>
:root{
  --red:#d02a2a;
  --red-dark:#b71f22;
  --ink:#2b2b2b;
  --muted:#666;
  --light:#f3f3f4;
  --footer:#222223;
  --footer-line:#3a3a3a;
  --white:#fff;
}
*{box-sizing:border-box;margin:0;padding:0}
html,body{width:1200px;height:2808px;overflow:hidden}
body{position:relative;background:var(--white);font-family:"Open Sans",sans-serif;color:var(--ink)}
.abs{position:absolute}
/* header */
.site-header{position:absolute;left:0;top:0;width:1200px;height:85px;background:var(--white);box-shadow:0 1px 4px rgba(0,0,0,.08);z-index:2}
.brand{position:absolute;left:97px;top:22px;font-family:"Poppins",sans-serif;font-weight:700;font-size:32px;color:var(--red);letter-spacing:.5px}
.main-nav{position:absolute;right:95px;top:31px;display:flex;font-size:15px;color:#333}
.main-nav a{color:inherit;text-decoration:none;padding:0 20px;border-left:1px solid #ddd}
.main-nav a:first-child{border-left:none}
.main-nav a:last-child{padding-right:0}
/* hero */
.hero{position:absolute;left:0;top:85px;width:1200px;height:532px;background:linear-gradient(100deg,#6e7580 0%,#9aa1aa 35%,#5b6570 70%,#3e4651 100%)}
.hero-title{position:absolute;left:686px;top:185px;padding:16px 26px;background:rgba(20,30,40,.55);font-family:"Poppins",sans-serif;font-weight:700;font-size:38px;line-height:46px;color:var(--white);white-space:nowrap}
.slider-arrow{position:absolute;top:268px;width:30px;height:30px;border-radius:50%;background:rgba(0,0,0,.55)}
/* welcome */
.welcome{position:absolute;left:0;top:617px;width:1200px;height:500px;background:linear-gradient(180deg,#fff 0%,#f5f6f8 100%)}
.section-title{font-family:"Poppins",sans-serif;font-weight:500;font-size:40px;text-align:center;color:#222}
.welcome .section-title{position:absolute;left:0;width:1200px;top:68px}
.lead{position:absolute;left:168px;width:864px;top:138px;font-size:11.5px;line-height:20px;text-align:center;color:#555}
.feature{position:absolute;top:300px;width:330px;height:100px}
.feature-icon{position:absolute;left:0;top:0;width:90px;height:90px;border-radius:50%;background:var(--red);display:flex;align-items:center;justify-content:center}
.feature h3{position:absolute;left:107px;top:2px;font-family:"Poppins",sans-serif;font-weight:400;font-size:19px;color:#333}
.feature p{position:absolute;left:107px;top:32px;width:205px;font-size:11px;line-height:20px;color:#666}
/* helping */
.helping{position:absolute;left:0;top:1117px;width:1200px;height:466px;overflow:hidden}
.helping-photo{position:absolute;left:0;top:0;width:1200px;height:466px;background:linear-gradient(90deg,#9bb3c6 0%,#c9d9e6 55%,#6f86a4 100%)}
.helping-panel{position:absolute;left:0;top:0}
.helping h2{position:absolute;left:97px;top:78px;font-family:"Poppins",sans-serif;font-weight:500;font-size:41px;line-height:46px;color:var(--white)}
.helping p{position:absolute;left:97px;width:460px;font-size:11.5px;line-height:20px;font-weight:600;color:var(--white)}
.btn-outline{position:absolute;left:97px;top:352px;width:120px;height:32px;border:2px solid var(--white);border-radius:16px;color:var(--white);font-size:11px;font-weight:700;display:flex;align-items:center;justify-content:center;gap:6px}
/* testimonial */
.testimonial{position:absolute;left:0;top:1583px;width:1200px;height:265px;background:var(--light)}
.avatar-ring{position:absolute;left:150px;top:56px;width:150px;height:150px;border-radius:50%;border:5px solid var(--red);border-top-color:transparent;border-right-color:transparent;transform:rotate(-10deg)}
.avatar{position:absolute;left:160px;top:60px;width:135px;height:135px;border-radius:50%;background:radial-gradient(circle at 50% 40%,#c7a58e,#6d5a4f);border:4px solid var(--white)}
.quote{position:absolute;left:328px;top:72px;width:740px;font-style:italic;font-size:13px;line-height:24px;color:#555}
.quote-author{position:absolute;left:330px;top:156px;font-style:italic;font-size:14px;color:var(--red)}
.dots{position:absolute;left:330px;top:192px;display:flex;gap:6px}
.dots span{width:24px;height:3px;background:#ccc}
.dots span:first-child{background:var(--red)}
.quote-mark{position:absolute;left:1010px;top:150px;font-family:Georgia,serif;font-size:70px;color:#ddd}
/* blog */
.blog .section-title{position:absolute;left:0;width:1200px;top:1900px}
.post{position:absolute;top:1990px;width:310px}
.post-img{position:absolute;left:0;top:15px;width:310px;height:168px}
.post-date{position:absolute;left:9px;top:0;width:65px;height:73px;background:var(--red);color:var(--white);text-align:center;font-family:"Poppins",sans-serif;line-height:1}
.post-date .m{display:block;font-size:10px;margin-top:10px}
.post-date .d{display:block;font-size:24px;font-weight:600;margin-top:2px}
.post-date .y{display:block;font-size:10px;margin-top:3px}
.post h3{position:absolute;left:0;top:198px;font-family:"Poppins",sans-serif;font-weight:400;font-size:16px;color:#333;white-space:nowrap}
.post-meta{position:absolute;left:0;top:232px;display:flex;align-items:center;gap:10px;font-size:11px;font-style:italic;color:#555}
.stars{color:#e3a21a;font-style:normal;letter-spacing:1px;font-size:10px}
.post p{position:absolute;left:0;top:258px;width:310px;font-size:11px;line-height:20px;color:#666}
/* footer */
.site-footer{position:absolute;left:0;top:2385px;width:1200px;height:423px}
.footer-col h4{position:absolute;top:100px;font-family:"Poppins",sans-serif;font-weight:500;font-size:19px;color:var(--white);white-space:nowrap}
.quick-links{position:absolute;left:97px;top:150px;list-style:none;font-size:12px;line-height:22px;color:#ddd}
.quick-links li::before{content:"›";margin-right:12px}
.contact-item{position:absolute;left:315px;display:flex;gap:14px;font-size:12.5px;line-height:20px;color:#ddd}
.quote-intro{position:absolute;left:633px;top:146px;width:462px;font-size:11px;line-height:19px;color:#ddd}
.field{position:absolute;height:42px;border:1px solid #bbb;color:#ddd;font-size:11px;padding:0 14px;display:flex;align-items:center}
.btn-signup{position:absolute;left:874px;top:247px;width:227px;height:42px;background:var(--red);color:var(--white);font-size:13px;font-weight:700;display:flex;align-items:center;justify-content:center}
.footer-bottom{position:absolute;left:0;top:348px;width:1200px;height:1px;background:var(--footer-line)}
.copyright{position:absolute;left:97px;top:378px;font-size:11px;color:#ddd}
.social{position:absolute;left:995px;top:371px;display:flex;gap:6px}
.social span{width:23px;height:23px;border:1px solid #aaa;border-radius:50%}
</style>
</head>
<body>

<header class="site-header">
  <div class="brand">Lindenkrügelhof</div>
  <nav class="main-nav"><a>Home</a><a>About Us</a><a>Services</a><a>Blog</a><a>Contact Us</a></nav>
</header>

<section class="hero">
  <div class="abs" role="img" aria-label="Photo of a smiling businesswoman with a laptop seated in an airport departure lounge" style="inset:0"></div>
  <div class="hero-title">LINDENKRÜGELHOF<br>AIRLINE PASSENGERS</div>
  <div class="slider-arrow" style="left:40px"><svg width="30" height="30" viewBox="0 0 30 30"><path d="M17 10l-5 5 5 5" stroke="#fff" stroke-width="2" fill="none"/></svg></div>
  <div class="slider-arrow" style="left:1126px"><svg width="30" height="30" viewBox="0 0 30 30"><path d="M13 10l5 5-5 5" stroke="#fff" stroke-width="2" fill="none"/></svg></div>
</section>

<section class="welcome">
  <div class="abs" role="img" aria-label="Faint background photo of an airliner on the tarmac" style="left:300px;top:40px;width:700px;height:420px;background:radial-gradient(ellipse at center,rgba(200,205,215,.25),rgba(255,255,255,0) 70%)"></div>
  <h2 class="section-title">Welcome To Lindenkrügelhof</h2>
  <p class="lead">Lorem ipsum dolor sit amet, consectetur adipiscing elit, sed do eiusmod tempor incididunt ut labore et dolore magna aliqua. Ut enim ad minim veniam, quis nostrud exercitation ullamco laboris nisi ut aliquip ex ea commodo consequat. Duis aute irure dolor in reprehenderit in voluptate velit esse cillum dolore eu fugiat nulla pariatur. Excepteur sint occaecat cupidatat non proident, sunt in culpa qui officia deserunt mollit anim id est laborum</p>

  <div class="feature" style="left:98px">
    <div class="feature-icon"><svg width="34" height="40" viewBox="0 0 34 40"><path d="M2 2h20l10 10v26H2z" fill="#fff"/><path d="M22 2v10h10" fill="#e6b3b3"/><path d="M8 20h18M8 26h18M8 32h12" stroke="#d02a2a" stroke-width="2.5"/></svg></div>
    <h3>Cases Of Delays</h3>
    <p>Lorem ipsum dolor sit amet, conseur adiiscing elit, sed do eiusmod tempor incididunt ut labore et dolore</p>
  </div>
  <div class="feature" style="left:450px">
    <div class="feature-icon"><svg width="44" height="40" viewBox="0 0 44 40"><circle cx="26" cy="13" r="10" fill="none" stroke="#fff" stroke-width="2.5"/><path d="M26 7v12M23 10h5M23 16h5" stroke="#fff" stroke-width="2"/><path d="M2 26h8l8 4h10l-4 4H16M10 34l14 4 16-12" fill="none" stroke="#fff" stroke-width="2.5" stroke-linejoin="round"/></svg></div>
    <h3>Denied Boarding</h3>
    <p>Lorem ipsum dolor sit amet, conseur adiiscing elit, sed do eiusmod tempor incididunt ut labore et dolore</p>
  </div>
  <div class="feature" style="left:802px">
    <div class="feature-icon"><svg width="40" height="40" viewBox="0 0 40 40"><path d="M36 4c-2-2-6 0-9 3l-6 6-16-4-3 3 13 7-6 6-5-1-2 2 6 4 4 6 2-2-1-5 6-6 7 13 3-3-4-16 6-6c3-3 5-7 3-9z" fill="#fff"/></svg></div>
    <h3>Cancelled Flights</h3>
    <p>Lorem ipsum dolor sit amet, conseur adiiscing elit, sed do eiusmod tempor incididunt ut labore et dolore</p>
  </div>
</section>

<section class="helping">
  <div class="helping-photo" role="img" aria-label="Photo of a stressed traveller covering his face at an airport window, plane taking off behind"></div>
  <svg class="helping-panel" width="1200" height="466" viewBox="0 0 1200 466"><defs><linearGradient id="panelGlow" x1="0" y1="0" x2="1" y2="1"><stop offset="0" stop-color="#e03a35" stop-opacity=".4"/><stop offset="1" stop-color="#a81a1d" stop-opacity=".5"/></linearGradient></defs><polygon points="0,0 642,0 550,466 0,466" fill="#d02a2a"/><polygon points="0,0 642,0 550,466 0,466" fill="url(#panelGlow)"/></svg>
  <h2>Helping Airline<br>Passengers</h2>
  <p style="top:195px">Sed ut perspiciatis unde omnis iste natus error sit voluptatem accusantium dolorue laudantium, totam rem aperiam, eaque ipsa quae ab illo inventore veritatis et quasi architecto beatae vitae dicta sunt explicabo. Nemo enim ipsam voluptatem quia voluptas sit aspernatur aut odit aut fugit, sed quia consequuntur</p>
  <p style="top:286px">Nemo enim ipsam voluptatem quia voluptas sit anatur aut odit aut fugit, sed quia consequuntur magni dolores eos qui ratione voluptatem sequi nesciunt</p>
  <div class="btn-outline">READ MORE <svg width="11" height="11" viewBox="0 0 11 11"><circle cx="5.5" cy="5.5" r="5.5" fill="#fff"/><path d="M4.5 3l2.5 2.5-2.5 2.5" stroke="#d02a2a" stroke-width="1.5" fill="none"/></svg></div>
</section>

<section class="testimonial">
  <div class="avatar-ring"></div>
  <div class="avatar" role="img" aria-label="Portrait photo of the quoted passenger"></div>
  <p class="quote">“ Sed ut perspiciatis unde omnis iste natus error sit voluptatem accusantium doloremque laudantium, totam rem aperiam, eaque ipsa quae ab illo inventore veritatis et quasi architecto beatae vitae dicta sunt explicabo. Nemo enim ipsam voluptatem quia voluptas sit aspernatur aut odit aut fugit, sed quia consequuntur</p>
  <div class="quote-author">Anna Meier - Lindenkrügelhof</div>
  <div class="dots"><span></span><span></span><span></span></div>
  <div class="quote-mark">”</div>
</section>

<section class="blog">
  <h2 class="section-title">Latest blog</h2>
  <article class="post" style="left:98px">
    <div class="post-img" role="img" aria-label="Photo of a man checking his phone in an airport terminal" style="background:linear-gradient(120deg,#8a9aad,#3e5f8f 60%,#c1c7cc)"></div>
    <div class="post-date"><span class="m">APRIL</span><span class="d">02</span><span class="y">2017</span></div>
    <h3>Nemo enim ipsam voluptatem</h3>
    <div class="post-meta"><span class="stars">★★★☆☆</span><span>🗨 No comments</span></div>
    <p>Sed ut perspiciatis unde omnis iste natus error sit uptatem accusantium doloremque laudantium, totam rem aperiam, eaque ipsa quae ab illo inventore veritatis</p>
  </article>
  <article class="post" style="left:444px">
    <div class="post-img" role="img" aria-label="Photo of a tired woman waiting on airport seats" style="background:linear-gradient(120deg,#4f5f79,#8f9bab 55%,#2f3d55)"></div>
    <div class="post-date"><span class="m">APRIL</span><span class="d">02</span><span class="y">2017</span></div>
    <h3>Nemo enim ipsam voluptatem</h3>
    <div class="post-meta"><span class="stars">★★★☆☆</span><span>🗨 No comments</span></div>
    <p>Sed ut perspiciatis unde omnis iste natus error sit uptatem accusantium doloremque laudantium, totam rem aperiam, eaque ipsa quae ab illo inventore veritatis</p>
  </article>
  <article class="post" style="left:790px">
    <div class="post-img" role="img" aria-label="Photo of a woman sitting with luggage in a bright terminal hall" style="background:linear-gradient(120deg,#b9c7d6,#e3e8ee 50%,#7f93aa)"></div>
    <div class="post-date"><span class="m">APRIL</span><span class="d">02</span><span class="y">2017</span></div>
    <h3>Nemo enim ipsam voluptatem</h3>
    <div class="post-meta"><span class="stars">★★★☆☆</span><span>🗨 No comments</span></div>
    <p>Sed ut perspiciatis unde omnis iste natus error sit uptatem accusantium doloremque laudantium, totam rem aperiam, eaque ipsa quae ab illo inventore veritatis</p>
  </article>
</section>

<footer class="site-footer">
  <svg class="abs" style="left:0;top:0" width="1200" height="423" viewBox="0 0 1200 423"><path d="M0 48Q600 -20 1200 48V423H0z" fill="#222223"/><path d="M0 48Q600 -20 1200 48" stroke="#d02a2a" stroke-width="4" fill="none"/></svg>
  <div class="footer-col"><h4 style="left:97px">QUICK LINK</h4></div>
  <ul class="quick-links"><li>Home</li><li>About Lindenkrügelhof</li><li>Services</li><li>Blog</li><li>Contact us</li></ul>

  <div class="footer-col"><h4 style="left:315px">CONTACT US</h4></div>
  <div class="contact-item" style="top:150px"><svg width="12" height="16" viewBox="0 0 12 16"><path d="M6 0a6 6 0 0 0-6 6c0 4 6 10 6 10s6-6 6-10a6 6 0 0 0-6-6z" fill="#ddd"/><circle cx="6" cy="6" r="2.2" fill="#222"/></svg><span>Lindenkrügelhof<br>8004 Zürich Switzerland</span></div>
  <div class="contact-item" style="top:206px"><svg width="14" height="14" viewBox="0 0 14 14"><path d="M3 0l3 3-2 2c1 2 3 4 5 5l2-2 3 3-2 3C6 14 0 8 0 3z" fill="#ddd"/></svg><span>Phone : 1 555 014 2087</span></div>
  <div class="contact-item" style="top:240px"><svg width="14" height="12" viewBox="0 0 14 12"><rect y="1" width="14" height="10" fill="#ddd"/><path d="M0 1l7 5 7-5" stroke="#222" fill="none"/></svg><span>Email : info@lindenkruegelhof.ch</span></div>

  <div class="footer-col"><h4 style="left:633px">GET A QUOTE</h4></div>
  <p class="quote-intro">Lorem ipsum dolor sit amet, consectetur adipiscing elit, sed do eiusmod tempor incididunt ut labore et dolore magna aliqua. Ut enim ad minim veniam,</p>
  <div class="field" style="left:633px;top:196px;width:228px">Name</div>
  <div class="field" style="left:874px;top:196px;width:227px">E - Mail</div>
  <div class="field" style="left:633px;top:247px;width:228px">Phone No</div>
  <div class="btn-signup">SIGNUP NOW</div>

  <div class="footer-bottom"></div>
  <div class="copyright">© 2017 Lindenkrügelhof.  All Rights Reserved.</div>
  <div class="social"><span></span><span></span><span></span><span></span></div>
</footer>

</body>
</html>
```